Brightfold Partners Website

Brightfold Partners Advisory Services is a company which provides specialised advise in carbon markets, climate policy, landscapes, resilience and change. We are based in Australia but the majority of our business is global. Our clients range from governments to large corporates and not for profit organisations.
Our focus is on developing the capabilities of government officials, business decision makers and land managers so they can better navigate the complexity of climate change and sustainability.
We are looking for a website that is consistent with the high end professional services which we provide to serious players.
I have attached two versions of our logo. I have also attached the back of our business card so you can get a sense of what we hand to potential clients.

Target Market(s)

Professional individuals, decision makers, board members etc, government officials.

Industry/Entity Type

Government

Number of Pages Required

4 page

Font styles to use
Serif
Sans Serif

Requirements
Must have
• Please provide
• 1. Home page
• 2. Service page template
• 3. Contact page
• 4. Lead expert profile page

```html
<!DOCTYPE html>
<html lang="en">
<head>
<meta charset="utf-8">
<title>Brightfold Partners</title>
<link rel="stylesheet" href="https://fonts.googleapis.com/css2?family=Cinzel:wght@400;600&family=Open+Sans:ital,wght@0,400;0,600;1,400&display=swap">
<style>
:root{
  --ink:#2e3136;
  --text:#3b3e43;
  --muted:#6c6f74;
  --blue:#2282cc;
  --blue-dark:#1a6eb0;
  --page:#e6e7ea;
  --dark:#2a2a2b;
  --white:#ffffff;
  --rule:#c9cbcf;
}
*{box-sizing:border-box;margin:0;padding:0}
html,body{width:1050px;height:1200px;overflow:hidden}
body{
  position:relative;
  font-family:"Open Sans",Arial,sans-serif;
  color:var(--text);
  background:radial-gradient(ellipse 700px 500px at 380px 260px,#f7f7f8 0%,#ecedef 55%,var(--page) 100%);
}
.abs{position:absolute}
.top-bar{left:0;top:0;width:1050px;height:10px;background:var(--dark)}

.brand{left:134px;top:44px;display:flex;align-items:center;gap:14px}
.brand-dot{width:52px;height:52px;border-radius:50%;background:#8a8d92}
.brand-name{font-family:"Cinzel",Georgia,serif;font-weight:400;font-size:27px;line-height:31px;letter-spacing:2px;color:var(--ink)}

.call{right:129px;top:46px;display:flex;align-items:center;gap:8px;font-size:15px;color:#55585d}
.call strong{font-family:Georgia,serif;font-weight:400;font-size:19px;color:var(--blue)}

.nav{left:590px;top:93px;display:flex;align-items:center;gap:0;font-size:11px;color:#55585d}
.nav a{color:inherit;text-decoration:none;margin-right:25px}
.nav .current{background:var(--blue);color:var(--white);border:1px solid var(--blue-dark);border-radius:3px;padding:2px 9px;font-size:12px;margin-right:21px}

.slider{left:132px;top:147px;width:786px;height:328px;background:var(--white);border:1px solid #dcdde0}
.slide-photo{left:10px;top:10px;width:766px;height:308px;background:linear-gradient(180deg,#6a7788 0%,#b9c3cd 35%,#8d7a6c 65%,#2b2c30 100%)}
.slide-caption{left:10px;top:286px;width:766px;height:32px;background:rgba(25,25,28,.72);color:var(--white);font-family:"Cinzel",Georgia,serif;font-weight:600;font-size:16px;letter-spacing:.5px;text-align:center;line-height:32px}
.slide-arrow{top:295px;width:33px;height:35px;background:#8f9195;display:flex;align-items:center;justify-content:center}

.card{top:505px;width:188px;height:228px;background:#f5f5f6;border:1px solid #fff;border-radius:3px;box-shadow:0 0 0 1px #e2e3e6}
.card-media{left:11px;top:11px;width:166px;height:108px;border:1px solid #d9dadd;border-radius:3px;background:#fff;padding:4px}
.card-media-fill{width:100%;height:100%;display:flex;align-items:center;justify-content:center;background:linear-gradient(180deg,#efeff0,#dcdddf)}
.card-media-fill.blue{background:linear-gradient(180deg,#2a8fda,#1d72c0)}
.card-title{left:14px;top:133px;width:170px;font-size:14.5px;line-height:17px;color:var(--blue)}
.card-desc{left:14px;top:175px;width:165px;font-size:9.5px;line-height:12.5px;color:var(--muted)}
.card-more{left:14px;top:209px;font-size:10px;color:var(--ink)}
.card-shadow{top:733px;width:70px;height:6px;border-radius:50%;background:radial-gradient(ellipse at center,rgba(0,0,0,.35),rgba(0,0,0,0) 70%)}

.welcome-title{left:139px;top:793px;font-size:19px;color:#55585d;font-weight:400}
.welcome-title span{font-family:"Cinzel",Georgia,serif;font-weight:600;font-size:19px;color:var(--ink)}
.rule-dotted{height:0;border-top:1px dotted #b4b6ba}
.welcome-text{left:140px;top:834px;width:530px;font-size:10.3px;line-height:15.9px;color:#2f3236;text-align:justify}
.welcome-more{left:594px;top:948px;font-size:10.5px;font-weight:600;color:var(--ink)}

.contact-title{left:730px;top:794px;font-size:18.5px;color:var(--blue)}
.field{left:730px;width:181px;background:#fff;border:1px solid #cfd1d4;border-radius:2px;font-style:italic;font-size:10px;color:#a9abaf;padding:5px 9px}
.submit{left:730px;top:947px;width:78px;height:20px;background:var(--blue);border:1px solid var(--blue-dark);border-radius:2px;color:#fff;font-size:11px;display:flex;align-items:center}
.submit span{flex:1;padding-left:7px}
.submit i{width:24px;height:100%;border-left:1px solid #5ea9e0;display:flex;align-items:center;justify-content:center}

.footer{left:0;top:999px;width:1050px;height:167px;background:var(--blue);border-top:2px solid #fff;box-shadow:0 -1px 0 #b9bbbf}
.foot-head{font-family:"Cinzel",Georgia,serif;font-weight:600;font-size:13px;letter-spacing:.8px;color:#fff}
.foot-rule{height:0;border-top:1px dotted rgba(255,255,255,.7)}
.foot-list{list-style:none;font-size:10px;color:#fff;line-height:18px}
.foot-list li::before{content:"›";margin-right:8px;margin-left:-1px}
.foot-div{top:1034px;width:1px;height:96px;background:rgba(0,0,0,.15);box-shadow:1px 0 0 rgba(255,255,255,.15)}
.info-row{display:flex;gap:14px;font-size:10px;color:#fff;line-height:17px}
.info-row svg{flex:none;margin-top:3px}
.map{left:505px;top:1069px;width:182px;height:76px;background:#fff;padding:4px}
.map div{width:100%;height:100%;background:linear-gradient(135deg,#e6e2d6,#cfd3cf 60%,#e9e3b8)}
.foot-brand{left:741px;top:1061px;display:flex;align-items:center;gap:10px}
.foot-brand .brand-dot{width:38px;height:38px;background:#9fc8ec}
.foot-brand .brand-name{color:#fff;font-size:20px;line-height:22px}

.bottom{left:0;top:1168px;width:1050px;height:32px;background:var(--dark);color:#e8e8e8;font-size:11px;text-align:center;line-height:32px}
</style>
</head>
<body>
<div class="abs top-bar"></div>

<div class="abs brand">
  <div class="brand-dot"></div>
  <div class="brand-name">BRIGHTFOLD<br>PARTNERS</div>
</div>

<div class="abs call">
  <svg width="26" height="26" viewBox="0 0 26 26"><circle cx="13" cy="13" r="11.5" fill="none" stroke="#2282cc" stroke-width="1.5"/><path d="M10 7c-2 1-2 4 0 8s5 5 7 4l-2-3-2 1c-1-1-2-3-2-4l1-1z" fill="none" stroke="#2282cc" stroke-width="1.3" stroke-linejoin="round"/></svg>
  Call Us Now: <strong>555-014-2680</strong>
</div>

<nav class="abs nav">
  <a class="current" href="#">Home</a>
  <a href="#">Our Services</a>
  <a href="#">Lead Expert Profile</a>
  <a href="#" style="margin-right:0">Contact Us</a>
</nav>

<section class="abs slider">
  <div class="abs slide-photo" role="img" aria-label="Photo of two business people shaking hands between office towers"></div>
  <div class="abs slide-caption">LORAM IPSUM DOLOR SIT AMET, CONSECTETUER ADIPISCING ELIT</div>
</section>
<div class="abs slide-arrow" style="left:129px"><svg width="14" height="18" viewBox="0 0 14 18"><path d="M10 2 3 9l7 7" fill="none" stroke="#fff" stroke-width="3"/></svg></div>
<div class="abs slide-arrow" style="left:888px"><svg width="14" height="18" viewBox="0 0 14 18"><path d="m4 2 7 7-7 7" fill="none" stroke="#fff" stroke-width="3"/></svg></div>

<svg class="abs" style="left:138px;top:610px" width="14" height="20" viewBox="0 0 14 20"><path d="M11 2 3 10l8 8" fill="none" stroke="#8e9094" stroke-width="3"/></svg>
<svg class="abs" style="left:896px;top:610px" width="14" height="20" viewBox="0 0 14 20"><path d="m3 2 8 8-8 8" fill="none" stroke="#8e9094" stroke-width="3"/></svg>

<article class="abs card" style="left:191px">
  <div class="abs card-media"><div class="card-media-fill blue" role="img" aria-label="Advisory group icon"></div></div>
  <h3 class="abs card-title" style="font-weight:400">Corporate Advisory on Carbon Markets</h3>
  <p class="abs card-desc">Lorem ipsum dolor sit amet, con ectetuer adipiscing elit...</p>
  <a class="abs card-more">Read More &nbsp;&gt;&gt;</a>
</article>
<article class="abs card" style="left:434px">
  <div class="abs card-media"><div class="card-media-fill">
    <svg width="70" height="60" viewBox="0 0 70 60"><rect x="4" y="4" width="52" height="36" fill="none" stroke="#2282cc" stroke-width="3"/><path d="M30 40v10M20 52h20" stroke="#2282cc" stroke-width="3"/><circle cx="42" cy="22" r="11" fill="#fff" stroke="#2282cc" stroke-width="3"/><path d="m50 30 14 14" stroke="#2282cc" stroke-width="5"/><path d="M36 27v-4M41 27v-8M46 27v-6" stroke="#2282cc" stroke-width="2.5"/></svg>
  </div></div>
  <h3 class="abs card-title" style="font-weight:400">Monitoring, Reporting &amp; Verification</h3>
  <p class="abs card-desc">Lorem ipsum dolor sit amet, con ectetuer adipiscing elit...</p>
  <a class="abs card-more">Read More &nbsp;&gt;&gt;</a>
</article>
<article class="abs card" style="left:677px">
  <div class="abs card-media"><div class="card-media-fill">
    <svg width="64" height="74" viewBox="0 0 64 74"><path d="M30 2v18" stroke="#2282cc" stroke-width="3"/><path d="M31 3h14l-4 5 4 5H31z" fill="#2282cc"/><path d="M2 34 32 20l30 14z" fill="#2282cc"/><rect x="4" y="36" width="56" height="5" fill="#2282cc"/><path d="M10 44v22M22 44v22M34 44v22M46 44v22M56 44v22" stroke="#2282cc" stroke-width="5"/><rect x="2" y="66" width="60" height="6" fill="#2282cc"/></svg>
  </div></div>
  <h3 class="abs card-title" style="font-weight:400">Institutional Arrangements</h3>
  <p class="abs card-desc">Lorem ipsum dolor sit amet, con ectetuer adipiscing elit...</p>
  <a class="abs card-more">Read More &nbsp;&gt;&gt;</a>
</article>
<div class="abs card-shadow" style="left:200px"></div><div class="abs card-shadow" style="left:300px"></div>
<div class="abs card-shadow" style="left:443px"></div><div class="abs card-shadow" style="left:543px"></div>
<div class="abs card-shadow" style="left:686px"></div><div class="abs card-shadow" style="left:786px"></div>

<h2 class="abs welcome-title">Welcome to <span>BRIGHTFOLD PARTNERS</span></h2>
<div class="abs rule-dotted" style="left:139px;top:824px;width:538px"></div>
<p class="abs welcome-text">Lorem ipsum dolor sit amet, consectetuer adipiscing elit, sed diam nonummy nibh euismod tincidunt ut laoreet dolore magna aliquam erat volutpat. Ut wisi enim ad minim veniam, quis nostrud exerci tation ullamcorper suscipit lobortis nisl ut aliquip ex ea commodo consequat. Duis autem vel eum iriure dolor in hendrerit in vulputate velit esse molestie consequat, vel illum dolore eu feugiat nulla facilisis at vero eros et accumsan et iusto odio dignissim qui blandit praesent luptatum zzril delenit augue duis dolore te feugait nulla facilisi.Lorem ipsum dolor sit amet, consectetuer adipiscing elit, sed diam nonummy nibh euismod tincidunt ut laoreet dolore magna aliquam erat volutpat.</p>
<a class="abs welcome-more">Read More &nbsp;&gt;&gt;</a>

<h2 class="abs contact-title" style="font-weight:400">Contact Us</h2>
<div class="abs rule-dotted" style="left:730px;top:824px;width:181px"></div>
<div class="abs field" style="top:834px;height:23px">Name:</div>
<div class="abs field" style="top:863px;height:23px">E-mail address:</div>
<div class="abs field" style="top:892px;height:46px">How can we help?</div>
<div class="abs submit"><span>Submit</span><i><svg width="12" height="10" viewBox="0 0 12 10"><path d="m1 5 3.5 3.5L11 1" fill="none" stroke="#fff" stroke-width="2.2"/></svg></i></div>

<footer class="abs footer"></footer>
<h4 class="abs foot-head" style="left:137px;top:1033px">QUICK LINKS</h4>
<div class="abs foot-rule" style="left:137px;top:1061px;width:95px"></div>
<ul class="abs foot-list" style="left:137px;top:1065px">
  <li>Home</li><li>Our Services</li><li>Lead Expert Profile</li><li>Contact Us</li>
</ul>
<div class="abs foot-div" style="left:255px"></div>

<h4 class="abs foot-head" style="left:288px;top:1033px">CONTACT INFORMATION</h4>
<div class="abs foot-rule" style="left:288px;top:1061px;width:148px"></div>
<div class="abs" style="left:284px;top:1066px;display:flex;flex-direction:column;gap:1px">
  <div class="info-row"><svg width="12" height="14" viewBox="0 0 12 14"><path d="M6 1a4.5 4.5 0 0 0-4.5 4.5C1.5 9 6 13.5 6 13.5S10.5 9 10.5 5.5A4.5 4.5 0 0 0 6 1z" fill="#fff"/><circle cx="6" cy="5.5" r="1.7" fill="#2282cc"/></svg><span>Lorem ipsum dolor sit amet,<br>consectetuer adipiscing elit</span></div>
  <div class="info-row"><svg width="12" height="12" viewBox="0 0 12 12"><path d="M2 1h3l1 3-2 1c1 2 2 3 3 3l1-2 3 1v3c-6 1-10-3-9-9z" fill="#fff"/></svg><span>555014268</span></div>
  <div class="info-row"><svg width="14" height="10" viewBox="0 0 14 10"><rect x=".5" y=".5" width="13" height="9" fill="#fff"/><path d="m.5 .5 6.5 5 6.5-5" fill="none" stroke="#2282cc"/></svg><span>info@brightfoldpartners.com</span></div>
</div>
<div class="abs foot-div" style="left:477px"></div>

<h4 class="abs foot-head" style="left:508px;top:1033px">LOCATION MAP</h4>
<div class="abs foot-rule" style="left:508px;top:1061px;width:176px"></div>
<div class="abs map"><div role="img" aria-label="Street map showing the office location"></div></div>
<div class="abs foot-div" style="left:710px"></div>

<div class="abs foot-brand">
  <div class="brand-dot"></div>
  <div class="brand-name">BRIGHTFOLD<br>PARTNERS</div>
</div>

<div class="abs bottom">Copyright © 2014 Brightfold Partners &nbsp; | &nbsp; All Rights Reserved</div>
</body>
</html>
```